KRT Civils*

we are a construction company specialising in Housing, Water Infrastructure and Roadworks
This is the description I would like to be added to the Flyer. I have
also attached a Picture
Krt Civils is a Construction Company specializing in Housing, Roadworks
and Water infrastructure. Krt has established itself firmly in the
Construction industry with branches all through Southern Africa as well
as into Africa.
Krt is committed to giving its Clients efficient and Professional
service at all times, We pride ourselves on our ability to meet
deadlines and exceed expectations. Our aim is to establish Successful
Long lasting relationships with our Client base
Colors
Designer to choose only greyscale colors for use in the design.
Look and feel

```html
<!DOCTYPE html>
<html lang="en">
<head>
<meta charset="utf-8">
<title>KRT Civils Flyer</title>
<link href="https://fonts.googleapis.com/css2?family=Sorts+Mill+Goudy&display=swap" rel="stylesheet">
<style>
  :root {
    --page-bg: #f7f7f9;
    --paper: #efefef;
    --ink-dark: #1f1f1f;
    --rule: #2a2a2a;
    --panel: #878787;
    --panel-text: #ffffff;
    --band: #2b2b2b;
    --band-text: #cfcfcf;
    --logo-bg: #ffffff;
  }
  * { margin: 0; padding: 0; box-sizing: border-box; }
  html, body { width: 1200px; height: 1200px; overflow: hidden; background: var(--page-bg); }
  body { font-family: "Sorts Mill Goudy", Georgia, serif; position: relative; }

  .flyer {
    position: absolute; left: 210px; top: 50px;
    width: 766px; height: 1082px;
    background: var(--paper);
    transform: scale(1.017); transform-origin: 0 0;
    overflow: hidden;
  }
  .rule { position: absolute; left: 0; width: 100%; background: var(--rule); }
  .rule-top { top: 100px; height: 5px; }
  .rule-mid { top: 597px; height: 7px; }
  .rule-bottom { top: 982px; height: 4px; }

  .hero {
    position: absolute; left: 0; top: 113px; width: 100%; height: 480px;
    background: linear-gradient(180deg, #b9c4cf 0%, #7f8c99 18%, #8d7a70 30%, #c48a74 45%, #b7a07e 62%, #9c955c 80%, #8f8a4e 100%);
  }

  .brand {
    position: absolute; left: 80px; top: 70px; width: 600px; height: 75px;
    background: var(--logo-bg);
    display: flex; align-items: center; justify-content: center;
    font-size: 54px; letter-spacing: 4px; color: var(--ink-dark);
  }

  .about {
    position: absolute; left: 80px; top: 563px; width: 605px; height: 372px;
    background: var(--panel); border-radius: 36px;
    color: var(--panel-text);
    display: flex; padding: 26px 0 0 0;
  }
  .about-col { font-size: 22.5px; line-height: 28.3px; }
  .about-col.intro { width: 285px; padding-left: 48px; }
  .about-col.promise { width: 285px; padding-left: 28px; }
  .about-divider { width: 2px; height: 250px; margin-top: 20px; background: #7a7a7a; }
  .about strong { font-weight: normal; text-shadow: 0.5px 0 0 currentColor; }

  .contact-band {
    position: absolute; left: 0; top: 992px; width: 100%; height: 90px;
    background: var(--band); color: var(--band-text);
    display: flex; align-items: center;
  }
  .phone { display: flex; align-items: center; margin-left: 92px; font-size: 44px; letter-spacing: 1px; }
  .phone svg { width: 32px; height: 32px; margin-right: 8px; }
  .web { margin-left: 56px; font-size: 17px; line-height: 21px; }
  .web span { display: flex; align-items: center; }
  .web svg { width: 11px; height: 11px; margin-right: 6px; }
</style>
</head>
<body>
<main class="flyer">
  <div class="hero" role="img" aria-label="Photo of a new housing development with rows of small homes, power poles and hills behind"></div>
  <div class="rule rule-top"></div>
  <div class="brand">KRT Civils</div>
  <div class="rule rule-mid"></div>

  <section class="about">
    <p class="about-col intro"><strong>Krt Civils</strong> is a Construction Company specializing in Housing, Roadworks and Water infrastructure. Krt has established itself firmly in the Construction industry with branches all through Southern Africa as well as into Africa.</p>
    <div class="about-divider"></div>
    <p class="about-col promise">Krt is committed to giving its Clients efficient and Professional service at all times, We pride ourselves on our ability to meet deadlines and exceed expectations. Our aim is to establish Successful Long lasting relationships with our Client base</p>
  </section>

  <div class="rule rule-bottom"></div>
  <footer class="contact-band">
    <div class="phone">
      <svg viewBox="0 0 32 32" fill="none" stroke="currentColor" stroke-width="2.4" stroke-linecap="round">
        <path d="M8 4l5 6-3 3c1.5 3.5 4.5 6.5 8 8l3-3 6 5-3 4C14 26 6 18 4 8z" fill="currentColor" stroke="none"/>
        <path d="M18 9a6 6 0 0 1 5 5M18 4a11 11 0 0 1 10 10"/>
      </svg>
      002 5550 1234
    </div>
    <div class="web">
      <span><svg viewBox="0 0 12 12"><rect x="1" y="2.5" width="10" height="7" fill="none" stroke="currentColor" stroke-width="1.3"/><path d="M1 3l5 4 5-4" fill="none" stroke="currentColor" stroke-width="1.2"/></svg>info@krtcivils.com</span>
      <span><svg viewBox="0 0 12 12"><circle cx="6" cy="6" r="5" fill="currentColor"/></svg>www.krtcivils.com</span>
    </div>
  </footer>
</main>
</body>
</html>
```